Quorvex IT Service Management Business Card Design

We need a business card design for an IT Service Management consulting company that is a certified partner of an ITSM software vendor.
The company name: Quorvex
Vendor whom Quorvex is a certified partner of: BrightPlume
Visit http://www.quorvexitsm.example
Visit http://www.brightplume.example
Industry/Entity Type
Software
Contact Information for Business Card
Front Content: (blue and white)
- Quorvex Logo (attached)
- Quorvex
- IT Service Management
- Dale Marbury
- (555) 310-4827 - office
- (555) 862-0593 - mobile
- dale@quorvexitsm.example
- www.quorvexitsm.example
- 2870 Orchardvale Pkwy., #6021
Lilburn, GA 30099
Back Content: (blue and green)
- Brightplume Prime Certified partner logo (attached)
- IT Service Management
- IT Asset Management
- IT Financial Management
(place the 3 items above in blocks of different colors - see attached sample)
Look and feel
Each slider illustrates characteristics of the customer's brand and the style your logo design should communicate.

```html
<!DOCTYPE html>
<html lang="en">
<head>
<meta charset="UTF-8">
<title>Quorvex Business Card</title>
<link href="https://fonts.googleapis.com/css2?family=Montserrat:wght@400;600;700&display=swap" rel="stylesheet">
<style>
  :root {
    --brand-blue: #234c87;
    --accent-blue: #a9bcd6;
    --card-white: #ffffff;
    --backdrop: #ebebec;
    --text-light: #ffffff;
  }
  * { margin: 0; padding: 0; box-sizing: border-box; }
  html, body {
    width: 1200px;
    height: 718px;
    overflow: hidden;
    background: var(--backdrop);
    font-family: "Montserrat", Arial, sans-serif;
  }
  .canvas {
    position: relative;
    width: 1200px;
    height: 718px;
  }
  .business-card {
    position: absolute;
    left: 250px;
    top: 159px;
    width: 700px;
    height: 400px;
    background: var(--card-white);
    overflow: hidden;
    box-shadow: 0 10px 30px rgba(0,0,0,0.12);
  }
  .card-shape {
    position: absolute;
    inset: 0;
  }
  .contact-panel {
    position: absolute;
    left: 44px;
    top: 48px;
    color: var(--text-light);
  }
  .person-name {
    font-size: 22px;
    font-weight: 600;
    letter-spacing: 1px;
    text-transform: uppercase;
  }
  .person-title {
    font-size: 14px;
    margin-top: 4px;
  }
  .address {
    margin-top: 40px;
    font-size: 13px;
    line-height: 1.55;
  }
  .contact-list {
    list-style: none;
    margin-top: 44px;
    font-size: 12.5px;
  }
  .contact-list li {
    display: flex;
    align-items: center;
    gap: 10px;
    margin-bottom: 9px;
  }
  .contact-icon {
    width: 14px;
    height: 14px;
    flex: none;
  }
  .brand-block {
    position: absolute;
    left: 420px;
    top: 120px;
    color: var(--brand-blue);
    text-align: left;
  }
  .brand-row {
    display: flex;
    align-items: center;
    gap: 10px;
  }
  .brand-dot {
    width: 22px;
    height: 22px;
    border-radius: 50%;
    background: var(--brand-blue);
  }
  .brand-name {
    font-size: 48px;
    font-weight: 700;
    line-height: 1;
    letter-spacing: -0.5px;
  }
  .brand-tagline {
    margin-top: 8px;
    margin-left: 32px;
    font-size: 13px;
    font-weight: 600;
  }
</style>
</head>
<body>
<main class="canvas">
  <section class="business-card" aria-label="Quorvex business card front">
    <svg class="card-shape" viewBox="0 0 700 400" width="700" height="400" aria-hidden="true">
      <path d="M0,0 H318 C400,90 330,300 470,400 H0 Z" fill="var(--accent-blue)"/>
      <path d="M0,0 H300 C380,90 310,300 450,400 H0 Z" fill="var(--brand-blue)"/>
    </svg>

    <div class="contact-panel">
      <h1 class="person-name">Dale Marbury</h1>
      <p class="person-title">Managing Director</p>
      <p class="address">2870 Orchardvale Pkwy., #6021<br>Lilburn, GA 30099</p>
      <ul class="contact-list">
        <li>
          <svg class="contact-icon" viewBox="0 0 14 14" aria-hidden="true"><path d="M3 1 L5 4 L4 5.5 C5 7.5 6.5 9 8.5 10 L10 9 L13 11 L12 13 C6 13 1 8 1 2 Z" fill="#fff"/></svg>
          (555) 310-4827
        </li>
        <li>
          <svg class="contact-icon" viewBox="0 0 14 14" aria-hidden="true"><rect x="3.5" y="1" width="7" height="12" rx="1.2" fill="none" stroke="#fff" stroke-width="1.4"/><circle cx="7" cy="11" r="0.8" fill="#fff"/></svg>
          (555) 862-0593
        </li>
        <li>
          <svg class="contact-icon" viewBox="0 0 14 14" aria-hidden="true"><rect x="1" y="3" width="12" height="8" fill="#fff"/><path d="M1 3 L7 8 L13 3" fill="none" stroke="var(--brand-blue)" stroke-width="1.2"/></svg>
          dale@quorvexitsm.example
        </li>
        <li>
          <svg class="contact-icon" viewBox="0 0 14 14" aria-hidden="true"><circle cx="7" cy="7" r="5.8" fill="none" stroke="#fff" stroke-width="1.3"/><ellipse cx="7" cy="7" rx="2.5" ry="5.8" fill="none" stroke="#fff" stroke-width="1"/><line x1="1.2" y1="7" x2="12.8" y2="7" stroke="#fff" stroke-width="1"/></svg>
          www.quorvexitsm.example
        </li>
      </ul>
    </div>

    <div class="brand-block">
      <div class="brand-row">
        <span class="brand-dot" aria-hidden="true"></span>
        <span class="brand-name">Quorvex</span>
      </div>
      <p class="brand-tagline">IT Service Management</p>
    </div>
  </section>
</main>
</body>
</html>
```